PDF flyer for our companies' two main products: Food processing machines.

PDF flyer with showcasing two products. Flyer can be one page per product, or both products on the same page.

Product #1: Labeled "Ribbon blenders".
Showing a photo of the machine, and the details/features offered with that machine. Product description must also say: "Sizes available; 2 Cu Ft. - 450 Cu Ft."

Product #2: Labeled: " Auger hoppers / Screw feeders"
Showing a photo of the machine, and the details/features offered with that machine.

SEE UPLOADED IMAGES; "Ribbon Blenders EXAMPLE FLYER".
& "Auger Hoppers / Screw Conveyors EXAMPLE FLYER" for a rough idea of what we are looking for.

Target Market(s)

Copackers, Packing houses, Food manufacturers, protein powder producers,

Industry/Entity Type

Commercial Food processing / packing / mixing equipment

Font styles to use
Serif

Colors
0054AA
0677BA
7BADD7
CADEEF
E8F1F8

Requirements
Must have
• Company logo on top of flyer.
Nice to have
• I would like for the flyer to show some stock images of common ingredients, similar to the images uploaded.
Should not have
• Pictures with background. Backgrounds must be removed from provides photos. "clipping path"

```html
<!DOCTYPE html>
<html lang="en">
<head>
<meta charset="utf-8">
<title>Kestrel Equipment – Product Flyers</title>
<link href="https://fonts.googleapis.com/css2?family=Montserrat:wght@500;600;700;800&family=Barlow+Condensed:wght@600;700&family=Roboto:wght@400;500&display=swap" rel="stylesheet">
<style>
:root{
  --ink:#111214;
  --blue:#1b6fa8;
  --blue-deep:#0054aa;
  --blue-mid:#0677ba;
  --blue-soft:#7badd7;
  --blue-pale:#cadeef;
  --blue-mist:#e8f1f8;
  --band:#e1e2e3;
  --paper:#ffffff;
  --canvas:#eceef0;
  --text:#1d1f22;
}
*{box-sizing:border-box;margin:0;padding:0}
html,body{width:783px;height:1200px;overflow:hidden;background:var(--canvas)}
body{position:relative;font-family:'Montserrat',sans-serif;color:var(--text)}

.flyer{position:absolute;width:310px;height:440px;background:var(--paper);transform-origin:0 0;box-shadow:0 2px 8px rgba(0,0,0,.18);overflow:hidden}
.flyer--hero{left:255px;top:90px;transform:scale(1.113)}
.flyer--blender{left:51px;top:669px}
.flyer--auger{left:415px;top:666px;transform:scale(1.013)}

.abs{position:absolute}
.header-art{position:absolute;left:0;top:0}

.brand{position:absolute;display:flex;align-items:center;gap:3px;font-family:'Montserrat',sans-serif;font-weight:800;color:var(--ink);letter-spacing:.5px}
.brand-dot{width:7px;height:7px;border-radius:50%;background:var(--blue)}

.title{position:absolute;font-family:'Montserrat',sans-serif;font-weight:800;color:#fff;white-space:nowrap;letter-spacing:.3px}
.title .accent{color:var(--blue)}

.sizes{position:absolute;left:46px;top:47px;width:219px;height:16px;border:1px solid var(--ink);border-radius:5px;display:flex;align-items:center;justify-content:center;gap:6px;white-space:nowrap}
.sizes-label{font-family:'Barlow Condensed',sans-serif;font-weight:700;font-size:12px;color:var(--ink)}
.sizes-label .accent{color:var(--blue)}
.sizes-range{font-weight:700;font-size:9.5px;color:var(--ink)}

.tab{position:absolute;height:16px;background:var(--blue);color:#fff;font-family:'Barlow Condensed',sans-serif;font-weight:700;font-size:9px;display:flex;align-items:center;padding-left:7px;border-radius:0 8px 8px 0;letter-spacing:.2px}

.ticks{position:absolute;list-style:none;font-weight:600;font-size:4.6px;line-height:1.15;color:var(--ink)}
.ticks li{position:relative;padding-left:7px}
.ticks li::before{content:"";position:absolute;left:0;top:.2px;width:4.4px;height:4.4px;border-radius:50%;background:var(--blue)}
.ticks li::after{content:"";position:absolute;left:1.4px;top:1.1px;width:1.2px;height:2px;border:solid #fff;border-width:0 .6px .6px 0;transform:rotate(45deg)}

.photo{position:absolute}
.photo--steel{background:radial-gradient(ellipse at 50% 40%,#d9dcdf 0%,#aeb3b8 55%,rgba(255,255,255,0) 78%)}
.photo--spices{background:linear-gradient(160deg,#2d2a28 0%,#7a3b1e 45%,#c7662a 70%,#3b3a30 100%);border:1.5px solid #fff;box-shadow:0 0 2px rgba(0,0,0,.4)}
.photo--nuts{background:radial-gradient(circle at 50% 55%,#7a4a2c 0%,#b88b62 35%,#fff 70%);border:1px solid var(--blue-mid)}
.photo--powder{background:radial-gradient(ellipse at 50% 70%,#b8853a 0%,#d4a55a 40%,rgba(255,255,255,0) 72%)}
.photo--thumb{border:.8px solid var(--blue-soft)}
.photo--ginger{background:radial-gradient(circle,#d9a866 0%,#fff 70%)}
.photo--seeds{background:radial-gradient(circle,#d8b88a 0%,#fff 72%)}
.photo--cumin{background:radial-gradient(circle,#8a6a44 0%,#fff 72%)}
.photo--pepper{background:radial-gradient(circle,#2a2220 0%,#fff 72%)}
.photo--anise{background:radial-gradient(ellipse,#8a4a26 0%,#b59a4a 40%,rgba(225,226,227,0) 75%)}

.band{position:absolute;background:var(--band)}

.spec{position:absolute;border:1px solid var(--blue);border-radius:6px;overflow:hidden;background:#fff}
.spec table{width:100%;border-collapse:collapse;font-family:'Roboto',sans-serif;color:var(--text)}
.spec th{background:var(--blue);color:#fff;font-family:'Montserrat',sans-serif;font-weight:700;text-align:center}
.spec td{white-space:nowrap}
.spec tr:nth-child(even) td{background:var(--blue-mist)}
.spec--blender table{font-size:3.3px}
.spec--blender th{font-size:3.6px;height:9px}
.spec--blender td{height:6px;padding:0 2px;border-left:.4px solid var(--blue-pale)}
.spec--auger table{font-size:4.6px}
.spec--auger th{font-size:4.6px;height:9px}
.spec--auger td{height:8.6px;padding:0 3px;border-left:.4px solid var(--blue-pale)}
.spec--auger td.wide{text-align:center}
.spec sup{font-size:60%}

.footer{position:absolute;left:0;right:0;bottom:0;background:var(--ink);display:flex;align-items:center;justify-content:center;color:#fff;font-weight:700;letter-spacing:1.6px}
.footer-rule{position:absolute;left:0;right:0;height:2px;background:var(--blue)}
</style>
</head>
<body>

<!-- Ribbon blender flyer, featured -->
<section class="flyer flyer--hero" aria-label="Ribbon blenders flyer">
  <svg class="header-art" width="310" height="44" viewBox="0 0 310 44" aria-hidden="true">
    <path d="M90 0 H102 C114 18 120 40 140 44 H128 C110 40 104 18 90 0Z" fill="#1b6fa8"/>
    <path d="M100 0 H310 V44 H140 C122 40 114 18 100 0Z" fill="#111214"/>
  </svg>
  <div class="brand" style="left:18px;top:15px;font-size:10px"><span class="brand-dot"></span>KESTREL</div>
  <h1 class="title" style="left:126px;top:14px;font-size:15.5px">RIBBON <span class="accent">BLENDERS</span></h1>
  <div class="sizes"><span class="sizes-label">SIZES <span class="accent">AVAILABLE</span></span><span class="sizes-range">2 Cu Ft. - 450 Cu Ft.</span></div>

  <div class="tab" style="left:15px;top:69px;width:109px">STANDARD FEATURES</div>
  <ul class="ticks" style="left:16px;top:92px;width:145px">
    <li style="margin-bottom:5.4px">304 stainless steel construction.</li>
    <li style="margin-bottom:4.4px">Pre-wired control panels with; batch timer, on/off switch, emergency stop button.</li>
    <li style="margin-bottom:5.4px">Food grade compression shaft seals.</li>
    <li style="margin-bottom:4.4px">Safety sensor on lid for autornatic shutoff when opened.</li>
    <li style="margin-bottom:5.4px">Air actuated discharge valve.</li>
    <li style="margin-bottom:5.4px">1 piece hinged lid with safety grating.</li>
    <li style="margin-bottom:5.4px">Power options; 220v/480v.</li>
    <li style="margin-bottom:5.4px">24" standard discharge height.</li>
    <li>Castor wheels on 53cf units and smaller</li>
  </ul>
  <div class="photo photo--steel" role="img" aria-label="Stainless steel ribbon blender with control box on a wheeled frame" style="left:162px;top:63px;width:130px;height:150px"></div>

  <div class="band" style="left:48px;top:208px;width:246px;height:82px"></div>
  <div class="photo photo--spices" role="img" aria-label="Spoons of colourful ground spices on a dark surface" style="left:16px;top:214px;width:70px;height:73px"></div>
  <div class="tab" style="left:96px;top:213px;width:64px">OPTIONS</div>
  <ul class="ticks" style="left:96px;top:235px;width:82px">
    <li style="margin-bottom:4.4px">Dual hinged lids available on custom orders.</li>
    <li style="margin-bottom:4.4px">Knife gate style discharge available on custom orders.</li>
    <li>Air purge seals available on custom orders.</li>
  </ul>
  <ul class="ticks" style="left:187px;top:235px;width:106px">
    <li style="margin-bottom:4.4px">316 stainless material available on custom orders.</li>
    <li style="margin-bottom:5.2px">Custom height modification.</li>
    <li style="margin-bottom:5.2px">Liquid spray systems</li>
    <li style="margin-bottom:5.2px">(VFD) Variable Frequency Drives</li>
    <li>Leg extensions</li>
  </ul>

  <div class="spec spec--blender" style="left:16px;top:299px;width:278px;height:102px">
    <table>
      <tr><th>MODEL SIZE</th><th>5cf</th><th>7CF</th><th>10.5CF</th><th>17.5CF</th><th>35CF</th><th>53CF</th><th>70.5CF</th><th>106CF</th></tr>
      <tr><td>Working Liters</td><td>120L</td><td>200L</td><td>300L</td><td>500L</td><td>1000L</td><td>1500L</td><td>2000L</td><td>3000L</td></tr>
      <tr><td>Fill Capicity</td><td>5CF / 150L</td><td>9CF / 250L</td><td>13CF / 375L</td><td>22CF / 625L</td><td>44CF / 1250L</td><td>66CF / 1875L</td><td>88CF / 2500L</td><td>132CF / 3750L</td></tr>
      <tr><td>Weight</td><td>440lbs</td><td>550lbs</td><td>770lbs</td><td>1212lbs</td><td>1874lbs</td><td>2645lbs</td><td>3527lbs</td><td>5511lbs</td></tr>
      <tr><td>Motor Size</td><td>4hp</td><td>5.3hp</td><td>6.7hp</td><td>10hp</td><td>14.75hp</td><td>20hp</td><td>25hp</td><td>30hp</td></tr>
      <tr><td>Total Length</td><td>50"</td><td>53.5"</td><td>63"</td><td>72"</td><td>94"</td><td>102"</td><td>131.5"</td><td>157.5"</td></tr>
      <tr><td>Total Width</td><td>28"</td><td>34"</td><td>41.5"</td><td>45"</td><td>52"</td><td>66"</td><td>52.5"</td><td>54"</td></tr>
      <tr><td>Total Height</td><td>66"</td><td>69"</td><td>71"</td><td>82"</td><td>87"</td><td>95"</td><td>76"</td><td>110"</td></tr>
      <tr><td>Tub Length</td><td>31.5"</td><td>35.5"</td><td>41"</td><td>47"</td><td>59"</td><td>70"</td><td>75"</td><td>100"</td></tr>
      <tr><td>Tub Width</td><td>16.5"</td><td>22"</td><td>25"</td><td>27.5"</td><td>35.5"</td><td>39"</td><td>48"</td><td>48"</td></tr>
      <tr><td>Tub Height</td><td>20.5"</td><td>26"</td><td>28"</td><td>33"</td><td>41"</td><td>46"</td><td>51"</td><td>53"</td></tr>
      <tr><td>Shaft Diameter</td><td>2"</td><td>2-1/4"</td><td>2-5/8"</td><td>3"</td><td>3.5"</td><td>4"</td><td>4"</td><td>5-1/4"</td></tr>
      <tr><td>Tub Thickness</td><td>3mm</td><td>3mm</td><td>3mm</td><td>4mm</td><td>4mm</td><td>5mm</td><td>5mm</td><td>6mm</td></tr>
      <tr><td>Ribbon Thickness</td><td>6mm</td><td>8mm</td><td>8mm</td><td>8mm</td><td>10mm</td><td>12mm</td><td>12mm</td><td>14mm</td></tr>
      <tr><td>Max RPM</td><td>46 rpm</td><td>46 rpm</td><td>46 rpm</td><td>46 rpm</td><td>30 rpm</td><td>31 rpm</td><td>32 rpm</td><td>33 rpm</td></tr>
    </table>
  </div>

  <div class="footer-rule" style="top:405px"></div>
  <footer class="footer" style="top:408px;font-size:8px">www.kestrelequipment.com</footer>
</section>

<!-- Ribbon blender flyer -->
<section class="flyer flyer--blender" aria-label="Ribbon blenders flyer">
  <svg class="header-art" width="310" height="44" viewBox="0 0 310 44" aria-hidden="true">
    <path d="M90 0 H102 C114 18 120 40 140 44 H128 C110 40 104 18 90 0Z" fill="#1b6fa8"/>
    <path d="M100 0 H310 V44 H140 C122 40 114 18 100 0Z" fill="#111214"/>
  </svg>
  <div class="brand" style="left:18px;top:15px;font-size:10px"><span class="brand-dot"></span>KESTREL</div>
  <h1 class="title" style="left:126px;top:14px;font-size:15.5px">RIBBON <span class="accent">BLENDERS</span></h1>
  <div class="sizes"><span class="sizes-label">SIZES <span class="accent">AVAILABLE</span></span><span class="sizes-range">2 Cu Ft. - 450 Cu Ft.</span></div>

  <div class="tab" style="left:15px;top:69px;width:109px">STANDARD FEATURES</div>
  <ul class="ticks" style="left:16px;top:92px;width:145px">
    <li style="margin-bottom:5.4px">304 stainless steel construction.</li>
    <li style="margin-bottom:4.4px">Pre-wired control panels with; batch timer, on/off switch, emergency stop button.</li>
    <li style="margin-bottom:5.4px">Food grade compression shaft seals.</li>
    <li style="margin-bottom:4.4px">Safety sensor on lid for autornatic shutoff when opened.</li>
    <li style="margin-bottom:5.4px">Air actuated discharge valve.</li>
    <li style="margin-bottom:5.4px">1 piece hinged lid with safety grating.</li>
    <li style="margin-bottom:5.4px">Power options; 220v/480v.</li>
    <li style="margin-bottom:5.4px">24" standard discharge height.</li>
    <li>Castor wheels on 53cf units and smaller</li>
  </ul>
  <div class="photo photo--steel" role="img" aria-label="Stainless steel ribbon blender with control box on a wheeled frame" style="left:162px;top:63px;width:130px;height:150px"></div>

  <div class="band" style="left:48px;top:208px;width:246px;height:82px"></div>
  <div class="photo photo--spices" role="img" aria-label="Spoons of colourful ground spices on a dark surface" style="left:16px;top:214px;width:70px;height:73px"></div>
  <div class="tab" style="left:96px;top:213px;width:64px">OPTIONS</div>
  <ul class="ticks" style="left:96px;top:235px;width:82px">
    <li style="margin-bottom:4.4px">Dual hinged lids available on custom orders.</li>
    <li style="margin-bottom:4.4px">Knife gate style discharge available on custom orders.</li>
    <li>Air purge seals available on custom orders.</li>
  </ul>
  <ul class="ticks" style="left:187px;top:235px;width:106px">
    <li style="margin-bottom:4.4px">316 stainless material available on custom orders.</li>
    <li style="margin-bottom:5.2px">Custom height modification.</li>
    <li style="margin-bottom:5.2px">Liquid spray systems</li>
    <li style="margin-bottom:5.2px">(VFD) Variable Frequency Drives</li>
    <li>Leg extensions</li>
  </ul>

  <div class="spec spec--blender" style="left:16px;top:299px;width:278px;height:102px">
    <table>
      <tr><th>MODEL SIZE</th><th>5cf</th><th>7CF</th><th>10.5CF</th><th>17.5CF</th><th>35CF</th><th>53CF</th><th>70.5CF</th><th>106CF</th></tr>
      <tr><td>Working Liters</td><td>120L</td><td>200L</td><td>300L</td><td>500L</td><td>1000L</td><td>1500L</td><td>2000L</td><td>3000L</td></tr>
      <tr><td>Fill Capicity</td><td>5CF / 150L</td><td>9CF / 250L</td><td>13CF / 375L</td><td>22CF / 625L</td><td>44CF / 1250L</td><td>66CF / 1875L</td><td>88CF / 2500L</td><td>132CF / 3750L</td></tr>
      <tr><td>Weight</td><td>440lbs</td><td>550lbs</td><td>770lbs</td><td>1212lbs</td><td>1874lbs</td><td>2645lbs</td><td>3527lbs</td><td>5511lbs</td></tr>
      <tr><td>Motor Size</td><td>4hp</td><td>5.3hp</td><td>6.7hp</td><td>10hp</td><td>14.75hp</td><td>20hp</td><td>25hp</td><td>30hp</td></tr>
      <tr><td>Total Length</td><td>50"</td><td>53.5"</td><td>63"</td><td>72"</td><td>94"</td><td>102"</td><td>131.5"</td><td>157.5"</td></tr>
      <tr><td>Total Width</td><td>28"</td><td>34"</td><td>41.5"</td><td>45"</td><td>52"</td><td>66"</td><td>52.5"</td><td>54"</td></tr>
      <tr><td>Total Height</td><td>66"</td><td>69"</td><td>71"</td><td>82"</td><td>87"</td><td>95"</td><td>76"</td><td>110"</td></tr>
      <tr><td>Tub Length</td><td>31.5"</td><td>35.5"</td><td>41"</td><td>47"</td><td>59"</td><td>70"</td><td>75"</td><td>100"</td></tr>
      <tr><td>Tub Width</td><td>16.5"</td><td>22"</td><td>25"</td><td>27.5"</td><td>35.5"</td><td>39"</td><td>48"</td><td>48"</td></tr>
      <tr><td>Tub Height</td><td>20.5"</td><td>26"</td><td>28"</td><td>33"</td><td>41"</td><td>46"</td><td>51"</td><td>53"</td></tr>
      <tr><td>Shaft Diameter</td><td>2"</td><td>2-1/4"</td><td>2-5/8"</td><td>3"</td><td>3.5"</td><td>4"</td><td>4"</td><td>5-1/4"</td></tr>
      <tr><td>Tub Thickness</td><td>3mm</td><td>3mm</td><td>3mm</td><td>4mm</td><td>4mm</td><td>5mm</td><td>5mm</td><td>6mm</td></tr>
      <tr><td>Ribbon Thickness</td><td>6mm</td><td>8mm</td><td>8mm</td><td>8mm</td><td>10mm</td><td>12mm</td><td>12mm</td><td>14mm</td></tr>
      <tr><td>Max RPM</td><td>46 rpm</td><td>46 rpm</td><td>46 rpm</td><td>46 rpm</td><td>30 rpm</td><td>31 rpm</td><td>32 rpm</td><td>33 rpm</td></tr>
    </table>
  </div>

  <div class="footer-rule" style="top:405px"></div>
  <footer class="footer" style="top:408px;font-size:8px">www.kestrelequipment.com</footer>
</section>

<!-- Auger hopper flyer -->
<section class="flyer flyer--auger" aria-label="Auger hoppers and screw conveyors flyer">
  <div class="abs" style="left:0;top:0;width:310px;height:47px;background:var(--ink)"></div>
  <div class="abs" style="left:0;top:47px;width:310px;height:2.5px;background:var(--blue)"></div>
  <h1 class="title" style="left:0;width:310px;text-align:center;top:16px;font-size:12.6px">AUGER HOPPERS / <span class="accent">SCREW CONVEYORS</span></h1>

  <div class="photo photo--steel" role="img" aria-label="Stainless steel auger hopper with inclined screw conveyor tube on a wheeled frame" style="left:196px;top:50px;width:104px;height:172px"></div>
  <div class="brand" style="left:196px;top:84px;font-size:11px"><span class="brand-dot"></span>KESTREL</div>

  <div class="tab" style="left:16px;top:74px;width:108px">STANDARD FEATURES</div>
  <ul class="ticks" style="left:16px;top:101px;width:90px">
    <li style="margin-bottom:6.4px">Direct Drive.</li>
    <li style="margin-bottom:6.4px">304 Stainless steel construction.</li>
    <li style="margin-bottom:6.4px">Stainless steel safety grating.</li>
    <li style="margin-bottom:6.4px">Pre-wired control panel.</li>
    <li style="margin-bottom:6.4px">Electric Vibrator.</li>
    <li>Castor Wheels.</li>
  </ul>
  <div class="photo photo--powder" role="img" aria-label="Pile of golden ground spice powder" style="left:76px;top:125px;width:100px;height:54px"></div>

  <div class="photo photo--thumb photo--ginger" role="img" aria-label="Fresh ginger root" style="left:16px;top:180px;width:40px;height:34px"></div>
  <div class="photo photo--thumb photo--seeds" role="img" aria-label="Coriander seeds" style="left:61px;top:180px;width:40px;height:34px"></div>
  <div class="photo photo--thumb photo--cumin" role="img" aria-label="Cumin seeds" style="left:105px;top:180px;width:40px;height:34px"></div>
  <div class="photo photo--thumb photo--pepper" role="img" aria-label="Black peppercorns" style="left:149px;top:180px;width:40px;height:34px"></div>

  <div class="band" style="left:16px;top:232px;width:280px;height:74px"></div>
  <div class="photo photo--nuts" role="img" aria-label="Whole nutmeg seeds, one cracked open" style="left:17px;top:235px;width:71px;height:69px"></div>
  <div class="tab" style="left:98px;top:235px;width:63px">OPTIONS</div>
  <ul class="ticks" style="left:98px;top:258px;width:88px">
    <li style="margin-bottom:4.6px">Square or round hopper. 3.5cf and 7cf hoppers are standard.</li>
    <li style="margin-bottom:4.6px">Custom hoppers up to 200cf.</li>
    <li>VFD (Variable Frequency Drive).</li>
  </ul>
  <ul class="ticks" style="left:189px;top:258px;width:100px">
    <li style="margin-bottom:4.6px">Clamshell Auger tube for easy cleanout.</li>
    <li>316 Stainless steel construction.</li>
  </ul>
  <div class="photo photo--anise" role="img" aria-label="Cardamom pods and star anise" style="left:190px;top:281px;width:96px;height:22px"></div>

  <div class="spec spec--auger" style="left:16px;top:324px;width:280px;height:72px">
    <table>
      <tr><th style="width:55px">MODEL</th><th>AH-A2</th><th>AH-A3</th><th>AH-A5</th><th>AH-A7</th><th>AH-A8</th><th>AH-A12</th></tr>
      <tr><td>FEEDING RATE</td><td>2m<sup>3</sup>/Hr</td><td>3m<sup>3</sup>/Hr</td><td>5m<sup>3</sup>/Hr</td><td>7m<sup>3</sup>/Hr</td><td>8m<sup>3</sup>/Hr</td><td>12m<sup>3</sup>/Hr</td></tr>
      <tr><td>PIPE DIAMETER</td><td>4"</td><td>4-1/2"</td><td>5-1/2"</td><td>6-1/4"</td><td>6-1/2"</td><td>8-1/2"</td></tr>
      <tr><td>HOPPER VOL.</td><td>3.5CF</td><td class="wide" colspan="5">7CF</td></tr>
      <tr><td>DIMENSIONS</td><td>28.6"x24.4"x31.5"</td><td class="wide" colspan="5">40" x 32" x 35"</td></tr>
      <tr><td>TOTAL WEIGHT</td><td>221LBS</td><td>287LBS</td><td>397LBS</td><td>441LBS</td><td>485LBS</td><td>596LBS</td></tr>
      <tr><td>CHARGING HEIGHT</td><td class="wide" colspan="6">STANDARD 72 INCHES. (40" - 196" AVAILABLE)</td></tr>
      <tr><td>CHARGING ANGLE</td><td class="wide" colspan="6">STANDARD 45° &nbsp;&nbsp;(30°-60° AVAILABLE)</td></tr>
    </table>
  </div>

  <div class="footer-rule" style="top:405px"></div>
  <footer class="footer" style="top:409px;font-size:8px">www.kestrelequipment.com</footer>
</section>

</body>
</html>
```